A4 Wholesale Catalogue for a Hardware Supply Company

We are a tarpaulin manufacture and supply company. We need a A4 multi page catalogue to be used as a selling tool for our wholesale customers. We want the catalogue to be easily understandable but also eye catching.

This catalogue will be used by local hardware stores to sell our products to their account customers. The idea of this catalogue is to enable the hardware store to have a snapshot of our products that will be relevant to their customers whom are largely builders. This will be not be given out to their customer and will be used only in store as a selling tool.

Industry/Entity Type

Building

Font styles to use
Serif

Requirements
Must have
• Detail as per supplied brief.
• Photos
• Branding
Should not have
• To many tables

```html
<!DOCTYPE html>
<html lang="en">
<head>
<meta charset="UTF-8">
<title>Meridian Tarps – Catalogue Cover</title>
<link rel="stylesheet" href="https://fonts.googleapis.com/css2?family=Didact+Gothic&display=swap">
<style>
  :root {
    --page-bg: #e9e4dc;
    --brand-blue: #416bb3;
    --accent-green: #6dbb2e;
    --white: #ffffff;
    --photo-site: #3a6fc9;
    --photo-roof: #2f5fcf;
    --photo-roof-green: #22a466;
    --photo-truck-red: #b8202a;
    --photo-truck-sky: #3f7fd6;
    --photo-truck-olive: #6f7a52;
    --photo-truck-wall: #c9c6c0;
  }
  * { box-sizing: border-box; margin: 0; padding: 0; }
  html, body {
    width: 1200px;
    height: 1200px;
    overflow: hidden;
    background: var(--page-bg);
  }
  .catalogue-cover {
    position: absolute;
    left: 211px;
    top: 50px;
    width: 778px;
    height: 1100px;
    background: var(--brand-blue);
    box-shadow: 0 4px 14px rgba(0,0,0,0.18);
    font-family: "Didact Gothic", "Century Gothic", sans-serif;
  }
  .photo-grid {
    display: grid;
    grid-template-columns: 389px 389px;
    grid-template-rows: 408px 408px;
  }
  .photo { width: 100%; height: 100%; }
  .photo--frame-site {
    background: linear-gradient(160deg, #d9c29a 0%, #c8ad7e 18%, var(--photo-site) 40%, #2a58b4 100%);
  }
  .photo--roof-cover {
    background: linear-gradient(180deg, #c9ccd4 0%, #9fb0cc 26%, #5c7a4e 34%, var(--photo-roof) 46%, var(--photo-roof-green) 66%, var(--photo-roof) 80%, #2648b8 100%);
  }
  .photo--bin-truck {
    background: linear-gradient(180deg, var(--photo-truck-sky) 0%, #2d5f9e 22%, var(--photo-truck-red) 34%, #961a22 70%, #3c3c3e 100%);
  }
  .photo--flatbed-truck {
    background: linear-gradient(180deg, var(--photo-truck-wall) 0%, #b8b3aa 14%, var(--photo-truck-olive) 24%, #5f6a45 64%, #3a3a3a 82%, #9a9893 100%);
  }
  .accent-rule {
    height: 8px;
    background: var(--accent-green);
  }
  .brand-band {
    position: relative;
    height: 276px;
  }
  .brand-name {
    position: absolute;
    left: 36px;
    top: 64px;
    display: flex;
    align-items: center;
    gap: 14px;
    color: var(--white);
    font-size: 50px;
    line-height: 1;
    letter-spacing: 0.5px;
  }
  .brand-dot {
    width: 16px;
    height: 16px;
    border-radius: 50%;
    background: var(--accent-green);
  }
  .tagline {
    position: absolute;
    left: 36px;
    top: 184px;
    color: var(--white);
    font-size: 24px;
    line-height: 1.2;
    text-transform: uppercase;
    letter-spacing: 0.2px;
  }
  .stockist-panel {
    position: absolute;
    left: 448px;
    top: 79px;
    width: 293px;
    height: 160px;
    background: var(--white);
    border-radius: 6px;
  }
</style>
</head>
<body>
  <main class="catalogue-cover">
    <section class="photo-grid">
      <div class="photo photo--frame-site" role="img" aria-label="Timber house frame on a slab covered with blue tarpaulin"></div>
      <div class="photo photo--roof-cover" role="img" aria-label="Blue and green tarpaulins covering a roof with suburbs behind"></div>
      <div class="photo photo--bin-truck" role="img" aria-label="Red rubbish removal truck with a black tarp over its load"></div>
      <div class="photo photo--flatbed-truck" role="img" aria-label="Flatbed truck with an olive canvas tarp tied over its load"></div>
    </section>
    <div class="accent-rule"></div>
    <section class="brand-band">
      <div class="brand-name"><span class="brand-dot"></span>Meridian Tarps</div>
      <p class="tagline">The largest range of<br>ready made tarps in Australia</p>
      <div class="stockist-panel"></div>
    </section>
  </main>
</body>
</html>
```